Therapy Dog Business need a brochure

I need a brochure designed for my Canine Assisted Therapy business in Victoria Australia. I have a logo already and info and photos to upload.
Best as white background and using the colours from the logo please
Updates

Hi Everyone,
I am sorry to have to revise the brief. I have added three new photos I was unable to add due to the size. I have had to wait for my photographer to change the size to add them today. I have been really inspired by all the work you have done so far. Thank you.
Could you please add the following on the brochure. (Under the individual dogs photo)
1. Pebble is the white dog. Please add the following under her picture. Pebble is one of the first Court Dogs in Australia. Working in Victoria, she has worked in the following Courts. The Inquest Tribunal of Norvale, The Petty Sessions Bench in Collingwood, and the Shire Tribunal in Melbourne CBD. Her ability to use her intuition for clients is inspiring. Please contact us for potential use in Courts. Pebble has worked at the Halden Constabulary College, and at KESTREL at Hal Con. She is a stunning dog!
2. Tobias is the golden dog. Tobias is Pebbles son, and had her instinct of intuition of who needs his help. Tobias has an incredible soft approach as does his mother Pebble. He is incredibly safe with young children, and yet has a playful nature for adolescents and adults alike. He is soft and caring, and like his mother will go to those who need him most. Tobias like his mother has worked at Halden Constabulary, his time at HC included the Halden Constabulary Command (HCC) Both he and his mother have very impressive CV'S!
3. Clover the black dog. Clover is my Therapy and Assistance dog "trainer" she is safe and stable with all the dogs and people I train for Therapy Dog Training and Assistance Dog Training. She has also been with me on my journey as a Counsellor and I have been able to work alongside her and Pebble for Counselling sessions.
She is soft, caring, and also intuitive. I am incredibly grateful for her help, as well as Pebble and Tobias.
ALSO I am so sorry to add this but could you also add the following: Maybe in dot point?
Court Dog Availability
Therapy Dog Visits - Lawyers - Courts - Child Protection
Police Station / Ambulance Station / Fire Station - Visits
Private Therapy Dog Sessions
website and email confirmation coming soon. Thank you

Target Market(s)

First Responders

Requirements
Must have
• All the photos provided.
Should not have
• Generic photos

```html
<!DOCTYPE html>
<html lang="en">
<head>
<meta charset="utf-8">
<title>Gentle Tails – Canine Assisted Therapy Brochure</title>
<link rel="stylesheet" href="https://fonts.googleapis.com/css2?family=Rubik:wght@500;600;700&family=Raleway:wght@400;500&family=Lobster&display=swap">
<style>
:root{
  --maroon:#923044;
  --orange:#f39c38;
  --blue:#8ea8e8;
  --pale:#e8edf8;
  --stage:#b3b3b8;
  --white:#ffffff;
}
*{box-sizing:border-box;margin:0;padding:0}
html,body{width:1200px;height:793px;overflow:hidden;background:var(--stage)}
body{position:relative;font-family:"Raleway",Arial,sans-serif}
.page{position:absolute;top:33px;width:564px;height:727px;background:var(--white);overflow:hidden}
.page--left{left:31px}
.page--right{left:605px}
.page__base{position:absolute;left:0;bottom:0;width:100%;height:9px;background:var(--maroon)}
.wave{position:absolute;left:0;bottom:9px;width:564px;height:120px}
.photo{position:absolute;background:linear-gradient(180deg,#b57058 0%,#c4876a 38%,#90a6e6 62%,#9db2ea 100%)}
.logo{position:absolute;border-radius:50%;background:var(--white);border:2px solid var(--maroon);display:flex;align-items:center;justify-content:center;font-family:"Rubik",Arial,sans-serif;font-weight:700;color:var(--maroon);text-align:center}
.abs{position:absolute}
.intro{left:243px;top:126px;width:321px;height:102px;background:var(--maroon);color:var(--white);font-size:9.2px;line-height:15.2px;padding:7px 10px;border-bottom:3px solid var(--orange)}
.hero-title{left:31px;top:164px;color:var(--white);font-family:"Rubik",Arial,sans-serif;font-weight:600;font-size:23px;line-height:27px}
.dog-card{position:absolute;top:296px;width:174px;height:195px;background:var(--pale);border-radius:5px;padding:8px 6px 0}
.dog-card__name{font-family:"Lobster",cursive;color:var(--orange);font-size:15px;line-height:18px;display:flex;align-items:center;gap:5px}
.dog-card__text{margin-top:6px;font-size:8.6px;line-height:12px;color:var(--maroon);text-align:justify}
.portrait{position:absolute;top:236px;width:84px;height:84px;border-radius:50%;border:2px solid var(--orange)}
.paw{width:11px;height:10px}
.benefits-title{left:0;width:564px;top:494px;text-align:center;font-family:"Rubik",Arial,sans-serif;font-weight:600;font-size:22px;color:var(--maroon)}
.benefit{position:absolute;top:531px;width:174px;height:168px;border-radius:6px;padding:6px 6px;color:var(--white)}
.benefit--orange{background:var(--orange)}
.benefit--maroon{background:var(--maroon)}
.benefit__title{font-family:"Rubik",Arial,sans-serif;font-weight:500;font-size:12px;line-height:15px;text-align:center;margin-bottom:3px}
.benefit__text{font-size:8.8px;line-height:13.8px;text-align:justify}
.why-title{left:18px;top:222px;font-family:"Rubik",Arial,sans-serif;font-weight:600;font-size:22.5px;line-height:27px;color:var(--maroon)}
.reason{position:absolute;left:211px;width:353px;background:var(--orange);border-radius:4px 0 0 4px;padding:2px 10px}
.reason__title{font-family:"Rubik",Arial,sans-serif;font-weight:600;font-size:12px;color:var(--maroon);line-height:15px}
.reason__text{font-size:8.8px;line-height:13.6px;color:var(--white)}
.availability{left:19px;top:366px;width:527px;height:126px;background:var(--pale);border-radius:10px;padding:8px 12px}
.availability__title{font-family:"Rubik",Arial,sans-serif;font-weight:600;font-size:22.5px;color:var(--maroon);line-height:26px}
.availability__list{list-style:none;margin-top:2px}
.availability__list li{display:flex;align-items:center;gap:12px;font-size:16.5px;line-height:26px;color:var(--maroon);font-weight:500}
.cta{left:80px;top:509px;width:404px;height:47px;background:var(--maroon);border-radius:7px;color:var(--white);font-family:"Rubik",Arial,sans-serif;font-weight:600;font-size:22px;display:flex;align-items:center;justify-content:center}
.cta-text{left:28px;top:563px;width:508px;text-align:center;font-size:10.6px;line-height:14px;color:var(--maroon)}
.phone{left:55px;top:650px;display:flex;align-items:center;gap:7px;font-family:"Rubik",Arial,sans-serif;font-weight:600;font-size:24px;color:var(--maroon)}
.icon-ring{width:26px;height:26px;border-radius:50%;border:1.5px solid var(--orange);display:flex;align-items:center;justify-content:center;background:var(--white)}
.divider{left:247px;top:631px;width:1px;height:74px;background:var(--maroon)}
.email{left:265px;top:635px;display:flex;align-items:center;gap:7px;font-size:16.5px;color:var(--maroon);font-weight:500}
.web{left:256px;top:669px;width:251px;height:32px;background:var(--maroon);border-radius:4px;color:var(--white);font-size:16.5px;font-weight:500;display:flex;align-items:center;justify-content:center}
</style>
</head>
<body>
<svg width="0" height="0" style="position:absolute">
  <defs>
    <symbol id="paw" viewBox="0 0 22 20">
      <ellipse cx="4" cy="8" rx="2.6" ry="3.2"/>
      <ellipse cx="8.5" cy="3.5" rx="2.6" ry="3.2"/>
      <ellipse cx="13.5" cy="3.5" rx="2.6" ry="3.2"/>
      <ellipse cx="18" cy="8" rx="2.6" ry="3.2"/>
      <path d="M11 9c-4 0-7 5-7 8 0 2 2 3 4 2.5 1.5-.4 2-.8 3-.8s1.5.4 3 .8c2 .5 4-.5 4-2.5 0-3-3-8-7-8z"/>
    </symbol>
  </defs>
</svg>

<!-- LEFT PAGE -->
<section class="page page--left">
  <svg class="wave" viewBox="0 0 564 120" preserveAspectRatio="none" aria-hidden="true">
    <path d="M0 80 C120 30 300 20 564 40 V120 H0 Z" fill="var(--pale)"/>
  </svg>

  <div class="photo" style="left:0;top:0;width:367px;height:200px" role="img" aria-label="Photo of two golden dogs and one black dog resting on a blue couch before a brick wall"></div>
  <svg class="abs" style="left:0;top:140px" width="300" height="110" viewBox="0 0 300 110" aria-hidden="true">
    <path d="M0 10 H300 V86 C240 92 200 98 120 104 C60 108 20 96 0 70 Z" fill="var(--orange)"/>
    <path d="M0 10 H250 V84 C190 94 130 100 70 98 C30 96 10 82 0 66 Z" fill="var(--blue)"/>
  </svg>
  <h1 class="abs hero-title">What is Canine<br>Assisted Therapy?</h1>

  <div class="logo" style="left:414px;top:12px;width:100px;height:100px;font-size:12px">Gentle<br>Tails</div>

  <p class="abs intro">Canine Assisted Therapy (CAT) is a unique form of therapy that integrates trained therapy dogs into the healing process.&nbsp; By working alongside licensed therapists, these compassionate and well-trained dogs help support individuals in overcoming emotional, physical, and psychological challenges.&nbsp; This innovative approach promotes healing, reduces stress, and enhances overall well-being.</p>

  <article class="dog-card" style="left:17px">
    <h2 class="dog-card__name">Pebble <svg class="paw" fill="var(--orange)"><use href="#paw"/></svg></h2>
    <p class="dog-card__text">Pebble is one of the first Court Dogs in Australia. Working in Victoria, she has worked in the following Courts. The Inquest Tribunal of Norvale, The Petty Sessions Bench in Collingwood, and the Shire Tribunal in Melbourne CBD. Her ability to use her intuition for clients is inspiring. Please contact us for potential use in Courts. Pebble has worked at the Halden Constabulary College, and at KESTREL at Hal Con. She is a stunning dog!</p>
  </article>
  <article class="dog-card" style="left:196px">
    <h2 class="dog-card__name">Tobias <svg class="paw" fill="var(--orange)"><use href="#paw"/></svg></h2>
    <p class="dog-card__text">Tobias is Pebbles son, and had her instinct of intuition of who needs his help. Tobias has an incredible soft approach as does his mother Pebble. He is incredibly safe with young children, and yet has a playful nature for adolescents and adults alike. He is soft and caring, and like his mother will go to those who need him most. Tobias like his mother has worked at Halden Constabulary, his time at HC included the Halden Constabulary Command (HCC) Both he and his mother have very impressive CV'S!</p>
  </article>
  <article class="dog-card" style="left:374px">
    <h2 class="dog-card__name">Clover <svg class="paw" fill="var(--orange)"><use href="#paw"/></svg></h2>
    <p class="dog-card__text">Clover is my Therapy and Assistance dog "trainer" she is safe and stable with all the dogs and people I train for Therapy Dog Training and Assistance Dog Training. She has also been with me on my journey as a Counsellor and I have been able to work alongside her and Pebble for Counselling sessions. She is soft, caring, and also intuitive. I am incredibly grateful for her help, as well as Pebble and Tobias.</p>
  </article>

  <div class="portrait" style="left:105px;background:linear-gradient(160deg,#9fb3ea,#d9b27a)" role="img" aria-label="Portrait of Pebble, a pale golden dog"></div>
  <div class="portrait" style="left:283px;background:linear-gradient(160deg,#c96a4a,#eadcc2)" role="img" aria-label="Portrait of Tobias, a cream golden dog"></div>
  <div class="portrait" style="left:461px;background:linear-gradient(160deg,#8ea8e8,#1c1c22)" role="img" aria-label="Portrait of Clover, a black dog"></div>

  <h2 class="abs benefits-title">Benefits of Canine Assisted Therapy.</h2>

  <div class="benefit benefit--orange" style="left:17px">
    <h3 class="benefit__title">Emotional Support<br>and Comfort.</h3>
    <p class="benefit__text">Therapy dogs provide immediate emotional support, offering comfort and companionship during therapy sessions. Their calming presence helps reduce feelings of anxiety, stress, and depression, and grief, creating a safe and nurturing environment for healing.</p>
  </div>
  <div class="benefit benefit--maroon" style="left:196px">
    <h3 class="benefit__title">Stress Relief and<br>Relaxation.</h3>
    <p class="benefit__text">Interacting with dogs has been proven to reduce cortisol (stress hormone) levels and increase serotonin and oxytocin, the “feel-good” hormones. This natural relief from stress makes Canine Assisted Therapy an ideal option for individuals dealing with anxiety, trauma, PTSD, and grief.</p>
  </div>
  <div class="benefit benefit--orange" style="left:374px">
    <h3 class="benefit__title" style="margin:7px 0 9px">Improved Mental Health.</h3>
    <p class="benefit__text">Therapy dogs encourage social interaction, communication, and emotional expression, helping individuals address mental health challenges such as depression, anxiety, PTSD, and grief.&nbsp; The unconditional love and companionship of a dog can foster trust and openness during therapy sessions.</p>
  </div>

  <div class="page__base"></div>
</section>

<!-- RIGHT PAGE -->
<section class="page page--right">
  <svg class="wave" viewBox="0 0 564 120" preserveAspectRatio="none" aria-hidden="true">
    <path d="M0 60 C80 10 140 0 230 40 C330 85 460 60 564 10 V120 H0 Z" fill="var(--pale)"/>
  </svg>

  <div class="photo" style="left:0;top:0;width:564px;height:172px" role="img" aria-label="Photo of two golden dogs and one black dog on a blue couch before a brick wall"></div>
  <div class="logo" style="left:138px;top:17px;width:116px;height:116px;font-size:14px">Gentle<br>Tails</div>

  <h2 class="abs why-title">Why Choose<br>Canine Assisted<br>Therapy?</h2>

  <div class="reason" style="top:180px;height:52px">
    <h3 class="reason__title">Proven Effectiveness</h3>
    <p class="reason__text">Studies and testimonials highlight the positive effects therapy dogs have on emotional, psychological and physical health.</p>
  </div>
  <div class="reason" style="top:234px;height:61px">
    <h3 class="reason__title">Non-Invasive and Gentle</h3>
    <p class="reason__text">Therapy dogs provide a natural and non-threatening way to engage with patients, making it accessible for individuals who may feel apprehensive about traditional therapy methods.</p>
  </div>
  <div class="reason" style="top:297px;height:52px">
    <h3 class="reason__title">Safe and Trustworthy</h3>
    <p class="reason__text">All therapy dogs are carefully trained to work with professionals, ensuring that interactions are safe, beneficial, and appropriate for all individuals.</p>
  </div>

  <div class="abs availability">
    <h2 class="availability__title">Court Dog Availability</h2>
    <ul class="availability__list">
      <li><svg class="paw" fill="var(--orange)"><use href="#paw"/></svg>Therapy Dog Visits - Lawyers - Courts - Child Protection</li>
      <li><svg class="paw" fill="var(--orange)"><use href="#paw"/></svg>Police Station / Ambulance Station / Fire Station - Visits</li>
      <li><svg class="paw" fill="var(--orange)"><use href="#paw"/></svg>Private Therapy Dog Sessions</li>
    </ul>
  </div>

  <div class="abs cta">Join the Healing Journey Today!</div>
  <p class="abs cta-text">Whether you are seeking emotional support or mental health improvement, Canine Assisted Therapy offers a unique and compassionate approach to healing.&nbsp; Connect with us today to learn more about how a therapy dog can help enhance your life and well-being.</p>

  <div class="abs phone">
    <span class="icon-ring"><svg width="13" height="13" viewBox="0 0 24 24" fill="var(--orange)"><path d="M6.6 10.8a15.1 15.1 0 0 0 6.6 6.6l2.2-2.2c.3-.3.7-.4 1-.2 1.1.4 2.3.6 3.6.6.6 0 1 .4 1 1V20c0 .6-.4 1-1 1A17 17 0 0 1 3 4c0-.6.4-1 1-1h3.5c.6 0 1 .4 1 1 0 1.3.2 2.5.6 3.6.1.3 0 .7-.2 1z"/></svg></span>
    0400 123 456
  </div>
  <div class="abs divider"></div>
  <div class="abs email">
    <span class="icon-ring"><svg width="13" height="10" viewBox="0 0 24 18" fill="none" stroke="var(--orange)" stroke-width="2"><rect x="1" y="1" width="22" height="16" rx="2" fill="var(--orange)"/><path d="M2 3l10 7 10-7" stroke="var(--white)"/></svg></span>
    info@gentletails.com.au
  </div>
  <div class="abs web">www.gentletails.com.au</div>

  <div class="page__base"></div>
</section>
</body>
</html>
```